Business Card Design Project

I have attached the logo and the colour pallete for the branding for the company.

Creative designs for business cards are needed.

The Company is modern corporate.

Industry/Entity Type

Business

```html
<!DOCTYPE html>
<html lang="en">
<head>
<meta charset="utf-8">
<title>Stepora Business Card</title>
<link href="https://fonts.googleapis.com/css2?family=Questrial&display=swap" rel="stylesheet">
<style>
  :root {
    --bg: #e7e4e1;
    --card: #ececec;
    --card-light: #ffffff;
    --purple: #5e2158;
    --purple-light: #692a61;
    --white: #ffffff;
  }
  * { margin: 0; padding: 0; box-sizing: border-box; }
  html, body {
    width: 1200px;
    height: 1181px;
    overflow: hidden;
    background: var(--bg);
    font-family: "Questrial", "Century Gothic", sans-serif;
  }
  .canvas { position: relative; width: 1200px; height: 1181px; }
  .card {
    position: absolute;
    left: 216px;
    width: 768px;
    height: 442px;
    border-radius: 30px;
    background: radial-gradient(ellipse at 50% 55%, var(--card-light) 0%, var(--card) 70%);
    box-shadow: 0 6px 14px rgba(0,0,0,0.25);
    overflow: hidden;
  }
  .card--front { top: 110px; }
  .card--back { top: 619px; }
  .tab {
    position: absolute;
    left: 121px;
    width: 527px;
    height: 16px;
    background: var(--purple);
  }
  .tab--top { top: 0; border-radius: 0 0 6px 6px; }
  .tab--bottom { bottom: 0; border-radius: 6px 6px 0 0; }
  .brand-name {
    color: var(--purple);
    font-size: 92px;
    line-height: 1;
    letter-spacing: -1px;
  }
  .card--front .brand-name {
    position: absolute;
    left: 0; right: 0;
    top: 170px;
    text-align: center;
  }
  .band {
    position: absolute;
    left: 0;
    top: 81px;
    width: 100%;
    height: 280px;
    background: radial-gradient(ellipse at 55% 50%, var(--purple-light) 0%, var(--purple) 75%);
  }
  .band .brand-name {
    position: absolute;
    color: var(--white);
    font-size: 70px;
    width: 260px;
    left: 52px;
    top: 140px;
    text-align: center;
    transform: translate(-50%, -50%) rotate(-90deg);
  }
  .contact {
    position: absolute;
    left: 481px;
    top: 78px;
    color: var(--white);
  }
  .contact__name { font-size: 28px; line-height: 1.1; }
  .contact__role { font-size: 21px; line-height: 1.1; margin-bottom: 10px; }
  .contact__line { font-size: 16px; line-height: 22px; }
</style>
</head>
<body>
<main class="canvas">
  <section class="card card--front">
    <div class="tab tab--top"></div>
    <div class="brand-name">stepora</div>
    <div class="tab tab--bottom"></div>
  </section>

  <section class="card card--back">
    <div class="tab tab--top"></div>
    <div class="band">
      <div class="brand-name">stepora</div>
      <div class="contact">
        <p class="contact__name">Your Name</p>
        <p class="contact__role">Director</p>
        <p class="contact__line">Your address line one</p>
        <p class="contact__line">Yourname@email.com</p>
        <p class="contact__line">www.website.com</p>
      </div>
    </div>
    <div class="tab tab--bottom"></div>
  </section>
</main>
</body>
</html>
```